Harborline Bridal Bakery Selling Method needs finishing touches to website.

We have a temporary website located at http://www.brivantomarketworks.com/ql/.
We are doing a responsive design and have created the architecture (layout). However, we need a professional makeover for the graphic elements and colors of the website. The website will be selling a sales course to mostly women who sell wedding cakes.
The photos within the posted website are for illustrative purposes. We will use our own photos after the website is redone.
We are open to changing the font styles, borders, header, and anything else as long as the layout is not changed.
Target Market(s)
75% women age 25-50 and men 30-60.
Industry/Entity Type
Architecture
Colors
Designer to choose colors to be used in the design.
Look and feel
Each slider illustrates characteristics of the customer's brand and the style your logo design should communicate.

```html
<!DOCTYPE html>
<html lang="en">
<head>
<meta charset="utf-8">
<title>Harborline Bridal Bakery Selling Method</title>
<link href="https://fonts.googleapis.com/css2?family=Lobster&family=Lora:ital,wght@0,400;1,400&family=Raleway:wght@400&display=swap" rel="stylesheet">
<style>
  :root {
    --page-bg: #f1e9e3;
    --panel: #ffffff;
    --rose: #e3919f;
    --rose-deep: #c9556a;
    --rose-light: #f9c0cb;
    --rose-pale: #fbd3da;
    --tan: #d8bea4;
    --ink: #2f2b2a;
    --ink-soft: #5a5553;
    --caption: #9a7856;
    --rule: #eadfd6;
    --box-bg: #f3f3f3;
    --red-accent: #e2423f;
  }
  * { box-sizing: border-box; margin: 0; padding: 0; }
  html, body { width: 1138px; height: 1200px; overflow: hidden; }
  body { background: var(--page-bg); font-family: "Lora", Georgia, serif; color: var(--ink); position: relative; }

  .top-band { position: absolute; left: 0; top: 0; width: 1138px; height: 26px; background: linear-gradient(#eab6bf, #f0cdd2); }

  .page { position: absolute; left: 142px; top: 55px; width: 854px; height: 1102px; background: var(--panel); box-shadow: 0 0 6px rgba(0,0,0,.08); }

  .brand { position: absolute; left: 12px; top: 30px; display: flex; align-items: center; gap: 12px; }
  .brand-mark { width: 44px; height: 44px; border-radius: 50%; background: var(--rose-pale); }
  .brand-name { font-family: "Lora", Georgia, serif; font-size: 21px; line-height: 1.15; color: var(--ink); width: 200px; }

  .phone { position: absolute; right: 29px; top: 47px; font-family: Arial, Helvetica, sans-serif; font-size: 18px; color: var(--rose-deep); }

  .main-nav { position: absolute; left: 9px; top: 110px; width: 836px; height: 44px; background: linear-gradient(#fbd0d8, #f6b1bd); border-top: 3px solid #fde3e8; border-bottom: 3px solid #fde3e8; display: flex; justify-content: center; align-items: center; gap: 50px; }
  .main-nav a { font-style: italic; font-size: 14px; color: var(--ink); text-decoration: none; }

  .video { position: absolute; left: 9px; top: 172px; width: 554px; height: 336px; border-radius: 4px; overflow: hidden; background: linear-gradient(100deg, #f3e6e6 0%, #f1c6cc 40%, #e8b3ba 62%, #8aa27c 82%, #5f7d58 100%); box-shadow: 0 8px 8px -6px rgba(0,0,0,.2); }
  .video-play { position: absolute; left: 275px; top: 138px; }
  .video-bar { position: absolute; left: 37px; top: 296px; width: 484px; height: 29px; background: rgba(120,110,110,.65); display: flex; align-items: center; font-family: Arial, sans-serif; font-size: 8px; color: #fff; }
  .video-bar .cell { height: 100%; display: flex; align-items: center; padding: 0 8px; border-right: 1px solid rgba(255,255,255,.25); }
  .track { flex: 1; height: 3px; background: #fff; margin: 0 10px; position: relative; }
  .track::before { content: ""; position: absolute; left: 0; top: 0; width: 43%; height: 3px; background: var(--rose-light); }
  .vol { width: 30px; height: 3px; background: var(--rose-light); margin-left: 6px; }

  .signup { position: absolute; left: 573px; top: 172px; width: 271px; height: 332px; background: var(--box-bg); border: 1px solid #dcdcdc; box-shadow: 0 6px 6px -5px rgba(0,0,0,.15); }
  .signup h2 { font-family: "Raleway", Arial, sans-serif; font-weight: 400; font-size: 16.5px; line-height: 23px; text-align: center; color: var(--ink-soft); margin: 32px 14px 0; }
  .signup h2 em { font-style: normal; color: var(--red-accent); }
  .field { position: absolute; left: 8px; width: 253px; height: 40px; background: #fff; display: flex; align-items: center; }
  .field .icon { width: 48px; height: 40px; background: var(--tan); display: flex; align-items: center; justify-content: center; }
  .field span { font-family: Arial, sans-serif; font-size: 13px; color: #b9b9b9; margin-left: 15px; }
  .field.user { top: 120px; }
  .field.mail { top: 167px; }
  .access { position: absolute; left: 8px; top: 220px; width: 254px; height: 39px; background: var(--rose-light); border: 1px solid #f3a8b6; font-family: Arial, sans-serif; font-weight: bold; font-size: 13.5px; color: #fde8ec; display: flex; align-items: center; justify-content: center; }
  .no-spam { position: absolute; left: 0; width: 100%; top: 285px; text-align: center; font-family: Arial, sans-serif; font-size: 11px; color: var(--red-accent); }

  .section-title { position: absolute; left: 9px; top: 534px; width: 836px; height: 43px; border-top: 4px double var(--rule); border-bottom: 4px double var(--rule); display: flex; align-items: center; padding-left: 9px; font-family: "Lobster", cursive; font-weight: 400; font-size: 15px; color: var(--ink-soft); }

  .card { position: absolute; top: 607px; width: 176px; }
  .card-photo { width: 174px; height: 107px; background: linear-gradient(120deg, #e7b23b, #3e8a8a 50%, #e7c250); }
  .card-text { height: 147px; }
  .card-lead { margin-top: 16px; font-style: italic; font-size: 11.6px; line-height: 16px; letter-spacing: -0.15px; color: var(--caption); }
  .card-body { margin-top: 6px; font-size: 11.6px; line-height: 16px; letter-spacing: -0.15px; color: var(--ink); }
  .read-more { margin-top: 16px; width: 174px; height: 35px; background: var(--rose-light); color: #fde8ec; font-family: Arial, sans-serif; font-size: 14px; display: flex; align-items: center; justify-content: center; }

  .press { position: absolute; left: 9px; top: 949px; width: 836px; height: 90px; border-top: 4px double var(--rule); display: flex; justify-content: space-around; align-items: center; }
  .press-badge { background: #c4c4c4; }

  .site-footer { position: absolute; left: 0; top: 1053px; width: 854px; height: 49px; background: var(--rose); display: flex; align-items: center; justify-content: space-between; padding: 0 12px; font-style: italic; font-size: 11.5px; color: #fff; }
  .site-footer nav a { color: #fff; text-decoration: none; }
  .site-footer nav .sep { margin: 0 6px; }
</style>
</head>
<body>
  <div class="top-band" role="img" aria-label="Scalloped pink awning border"></div>

  <div class="page">
    <header>
      <div class="brand">
        <div class="brand-mark"></div>
        <div class="brand-name">Opening Bridal Cake Sales</div>
      </div>
      <div class="phone">Phone: 555.014.2290</div>
    </header>

    <nav class="main-nav">
      <a href="#">Home</a>
      <a href="#">Who Is Lena Marsh</a>
      <a href="#">Why Lena Is Sharing Her Secrets</a>
      <a href="#">Contact</a>
    </nav>

    <div class="video" role="img" aria-label="Video still of pink striped paper straws in a glass jar">
      <svg class="video-play" width="36" height="40" viewBox="0 0 36 40"><path d="M2 2 L34 20 L2 38 Z" fill="#fff"/></svg>
      <div class="video-bar">
        <div class="cell"><svg width="10" height="10" viewBox="0 0 10 10"><path d="M1 0 L10 5 L1 10Z" fill="#fff"/></svg></div>
        <div class="cell" style="flex:1">00:01<div class="track"></div>04:23</div>
        <div class="cell" style="width:60px"><svg width="10" height="9" viewBox="0 0 10 9"><path d="M0 3h3l3-3v9l-3-3H0z" fill="#fff"/></svg><div class="vol"></div></div>
        <div class="cell" style="border-right:none;width:38px;justify-content:center"><svg width="14" height="14" viewBox="0 0 14 14" fill="none" stroke="#fff" stroke-width="1.8"><path d="M8 1h5v5M13 1L8 6M6 13H1V8M1 13l5-5"/></svg></div>
      </div>
    </div>

    <aside class="signup">
      <h2><em>FREE Videos</em> To Help You Sell More Wedding Cakes At Higher Prices... Immediately</h2>
      <div class="field user">
        <div class="icon"><svg width="18" height="18" viewBox="0 0 18 18" fill="#fff"><circle cx="9" cy="5" r="4"/><path d="M1 18c0-5 3.5-7 8-7s8 2 8 7z"/></svg></div>
        <span>username</span>
      </div>
      <div class="field mail">
        <div class="icon"><svg width="14" height="18" viewBox="0 0 14 18" fill="#fff"><path d="M3 8V5a4 4 0 0 1 8 0v3h-2V5a2 2 0 0 0-4 0v3z"/><rect x="0" y="8" width="14" height="10" rx="1"/></svg></div>
        <span>email</span>
      </div>
      <div class="access">GET INSTANT ACCESS</div>
      <p class="no-spam">No Spam. I Promise.</p>
    </aside>

    <h3 class="section-title">3 Leading-Edge Techniques for Convincing Brides to Choose You</h3>

    <article class="card" style="left:21px">
      <div class="card-photo" role="img" aria-label="Colourful painted-makeup portrait on a yellow background"></div>
      <div class="card-text">
        <p class="card-lead">In the first video, discover a sales growth secret that reveals the "Two Faces Of Your Wedding Cake Business."</p>
        <p class="card-body">One side of your face displays your "Internal Reality." It's how you run your business. Whether...</p>
      </div>
      <div class="read-more">READ MORE</div>
    </article>
    <article class="card" style="left:233px">
      <div class="card-photo" role="img" aria-label="Colourful painted-makeup portrait on a yellow background"></div>
      <div class="card-text">
        <p class="card-lead">In the first video, discover a sales growth secret that reveals the "Two Faces Of Your Wedding Cake Business."</p>
        <p class="card-body">One side of your face displays your "Internal Reality." It's how you run your business. Whether...</p>
      </div>
      <div class="read-more">READ MORE</div>
    </article>
    <article class="card" style="left:447px">
      <div class="card-photo" role="img" aria-label="Colourful painted-makeup portrait on a yellow background"></div>
      <div class="card-text">
        <p class="card-lead">In the first video, discover a sales growth secret that reveals the "Two Faces Of Your Wedding Cake Business."</p>
        <p class="card-body">One side of your face displays your "Internal Reality." It's how you run your business. Whether...</p>
      </div>
      <div class="read-more">READ MORE</div>
    </article>
    <article class="card" style="left:660px">
      <div class="card-photo" role="img" aria-label="Colourful painted-makeup portrait on a yellow background"></div>
      <div class="card-text">
        <p class="card-lead">In the first video, discover a sales growth secret that reveals the "Two Faces Of Your Wedding Cake Business."</p>
        <p class="card-body">One side of your face displays your "Internal Reality." It's how you run your business. Whether...</p>
      </div>
      <div class="read-more">READ MORE</div>
    </article>

    <div class="press" role="img" aria-label="Row of press outlet badges">
      <div class="press-badge" style="width:38px;height:38px"></div>
      <div class="press-badge" style="width:122px;height:22px"></div>
      <div class="press-badge" style="width:38px;height:38px;border-radius:50%"></div>
      <div class="press-badge" style="width:44px;height:38px"></div>
      <div class="press-badge" style="width:98px;height:38px"></div>
      <div class="press-badge" style="width:82px;height:38px"></div>
    </div>

    <footer class="site-footer">
      <span>Copyright © 2014 The Harborline Bakehouse. All Rights Reserved.</span>
      <nav><a href="#">Home</a><span class="sep">|</span><a href="#">Who Is Lena Marsh</a><span class="sep">|</span><a href="#">Why Lena Is Sharing Her Secrets</a><span class="sep">|</span><a href="#">Contact</a></nav>
    </footer>
  </div>
</body>
</html>
```